KRT,LLC

I need a flyer that has my company Logo on it as well as my book cover on it. I need for the flyer to read: "Ashes Under the Bridge" ~ A story of Money,Murder,Sex and family ties in the heart of the city. Read along as Curtis J. Hollow masterfully paint this Wilmington,Delaware tale like no other~The "T.K.V boys" clash in a rain of bullets against North sides own "Zinga boys."
At $14.99 you can own your own copy of "Ashes Under the Bridge."
Contact Curt Hollow @ 302-555-0147 to purchase your paper back copy.
OR
Visit:www.krtllcbooks.example
www.ashezunderthebridge.example
ashesunderthebridge24@mailbox.example
To purchase your order directly off line.
We accept paxo,CoinLeaf and debit cards for those individuals who wish to order on-line!

```html
<!DOCTYPE html>
<html lang="en">
<head>
<meta charset="utf-8">
<title>Ashes Under the Bridge – Flyer</title>
<link rel="stylesheet" href="https://fonts.googleapis.com/css2?family=Creepster&family=Alfa+Slab+One&family=PT+Sans:wght@400;700&family=Open+Sans:wght@400;600;700&display=swap">
<style>
  :root {
    --backdrop: #7d1417;
    --paper: #ffffff;
    --blood: #8e1a1c;
    --blood-bright: #d8231f;
    --royal: #2b3d98;
    --navy: #1f2a6e;
    --ink: #111111;
    --mist: #c9d3dc;
    --badge: #151a2c;
    --gold: #f2c230;
  }
  * { margin: 0; padding: 0; box-sizing: border-box; }
  html, body { width: 1200px; height: 1000px; overflow: hidden; }
  body { background: var(--backdrop); position: relative; font-family: "PT Sans", sans-serif; }

  .flyer {
    position: absolute; left: 235px; top: 30px; width: 729px; height: 940px;
    background: linear-gradient(180deg, var(--paper) 0%, var(--paper) 42%, #e7ecf1 62%, var(--mist) 80%, #b9c4cf 100%);
    overflow: hidden; box-shadow: 0 10px 30px rgba(0,0,0,.45);
  }
  .title-main {
    position: absolute; top: 30px; left: 0; width: 100%; text-align: center;
    font-family: "Creepster", cursive; font-size: 150px; line-height: 1; color: var(--blood);
    letter-spacing: 6px;
  }
  .title-sub {
    position: absolute; top: 212px; left: 0; width: 100%; text-align: center;
    font-family: "Alfa Slab One", serif; font-size: 38px; line-height: 1; color: var(--blood); letter-spacing: 1px;
  }
  .title-sub .accent { color: var(--royal); }
  .tagline {
    position: absolute; top: 268px; left: 0; width: 100%; text-align: center;
    font-family: "Open Sans", sans-serif; font-size: 19px; font-weight: 600; color: var(--ink);
  }
  .tagline .hot { color: var(--blood-bright); font-weight: 700; }
  .blurb {
    position: absolute; top: 292px; left: 60px; width: 609px; text-align: center;
    font-family: "Open Sans", sans-serif; font-size: 13.5px; line-height: 1.6; color: var(--ink);
  }
  .rivals {
    position: absolute; top: 352px; left: 0; width: 100%; text-align: center;
    font-family: "Open Sans", sans-serif; font-size: 22px; color: var(--ink);
  }

  .photo { position: absolute; }
  .photo-author { left: 15px; top: 537px; width: 195px; height: 200px; border-radius: 40% 40% 10% 30%;
    background: radial-gradient(circle at 55% 45%, #b9774e 0%, #8a5236 40%, rgba(220,220,225,0) 75%); }
  .photo-cash { left: 527px; top: 450px; width: 200px; height: 115px;
    background: radial-gradient(ellipse at 50% 50%, #8c9270 0%, #b7b99b 50%, rgba(230,232,236,0) 80%); }
  .photo-street { left: 440px; top: 555px; width: 289px; height: 195px;
    background: radial-gradient(ellipse at 70% 50%, #5c5650 0%, #8a8782 45%, rgba(210,215,220,0) 80%); }
  .photo-cover { left: 190px; top: 440px; width: 310px; height: 188px; transform: rotate(-4deg);
    background: linear-gradient(90deg, #2e3a9a 0%, #2e3a9a 48%, #1d2670 49%, #1d2670 51%, #3242a6 52%, #3a4ab0 100%);
    box-shadow: 4px 6px 12px rgba(0,0,0,.35); }

  .price-badge {
    position: absolute; left: 140px; top: 350px; width: 78px; height: 78px; border-radius: 50%;
    background: var(--badge); color: #fff; text-align: center;
    font-family: "Open Sans", sans-serif; font-weight: 700; line-height: 1.05; padding-top: 13px; transform: rotate(-8deg);
  }
  .price-badge .buy { color: var(--gold); font-size: 14px; display: block; }
  .price-badge .amount { font-size: 17px; display: block; }
  .price-badge .only { font-size: 12px; display: block; }

  .wave { position: absolute; left: 0; top: 0; width: 729px; height: 940px; }

  .offer { position: absolute; left: 0; width: 100%; text-align: center; font-family: "Open Sans", sans-serif; }
  .offer-line { top: 710px; font-size: 19px; color: var(--ink); }
  .offer-line strong { font-size: 24px; }
  .offer-title { top: 737px; font-size: 23px; font-weight: 700; color: var(--blood-bright); }
  .offer-contact { top: 766px; font-size: 30px; color: var(--ink); }
  .offer-contact strong { font-weight: 700; }
  .offer-paperback { top: 812px; font-size: 15px; color: #fff; }
  .offer-or { top: 842px; font-size: 15px; color: #fff; }
  .offer-sites { top: 868px; font-size: 13px; color: #fff; }
  .offer-sites span { margin: 0 55px; }
  .offer-direct { top: 886px; font-size: 13px; color: #fff; }

  .brand { position: absolute; left: 22px; top: 806px; display: flex; align-items: center; gap: 8px; }
  .brand-dot { width: 84px; height: 84px; border-radius: 50%; background: #000; border: 3px solid #fff; }
  .brand-name { font-family: "Open Sans", sans-serif; font-weight: 700; font-size: 14px; color: #fff; }

  .payment-strip {
    position: absolute; left: 0; bottom: 0; width: 100%; height: 27px; background: var(--navy);
    color: #fff; text-align: center; font-family: "Open Sans", sans-serif; font-size: 12.5px; line-height: 27px;
  }
</style>
</head>
<body>
  <main class="flyer">
    <h1 class="title-main">ASHES</h1>
    <h2 class="title-sub">UNDER THE <span class="accent">BRIDGE</span></h2>

    <p class="tagline">A story of <span class="hot">Money, Murder, Sex and family</span> ties in the heart of the city.</p>
    <p class="blurb">Read along as Curtis J. Hollow masterfully paint this Wilmington, Delaware tale like no other~The "T.K.V boys" clash in a rain of bullets against North sides own</p>
    <p class="rivals">"Zinga boys."</p>

    <div class="photo photo-author" role="img" aria-label="Photo of the author in sunglasses and a white cap"></div>
    <div class="photo photo-cash" role="img" aria-label="Photo of stacked cash bundles"></div>
    <div class="photo photo-street" role="img" aria-label="Photo of a Wilmington street sign and a man on the corner"></div>
    <div class="photo photo-cover" role="img" aria-label="Paperback book cover of Ashes Under the Bridge, front and back"></div>

    <div class="price-badge"><span class="buy">Buy</span><span class="amount">$14.99</span><span class="only">Only</span></div>

    <svg class="wave" viewBox="0 0 729 940" aria-hidden="true">
      <path d="M0,800 C300,815 520,805 729,700 L729,940 L0,940 Z" fill="#2b3d98"/>
    </svg>

    <p class="offer offer-line">At <strong>$14.99</strong> you can own your own copy of</p>
    <p class="offer offer-title">"Ashes Under the Bridge."</p>
    <p class="offer offer-contact">Contact Curt Hollow @ <strong>302-555-0147</strong></p>
    <p class="offer offer-paperback">to purchase your paper back copy.</p>
    <p class="offer offer-or">OR</p>
    <p class="offer offer-sites"><span>Visit: www.krtllcbooks.example</span><span>www.ashezunderthebridge.example</span></p>
    <p class="offer offer-direct">To purchase your order directly off line.</p>

    <div class="brand"><div class="brand-dot"></div><span class="brand-name">KRT,LLC</span></div>

    <p class="payment-strip">We accept paxo, CoinLeaf and debit cards for those individuals who wish to order on-line!</p>
  </main>
</body>
</html>
```